Real Estate Business Cards

Looking for a clean, sharp and professional look for our Real Estate investment Fund that invests in Multi Family Apartment buildings.

Target Market(s)

Real Estate Fund

Industry/Entity Type

Real Estate

Contact Information for Business Card

Company Description: Real Estate Investment Fund
Company Name: RKW Holdings
Name: Marcus Olvane
Cell: (917) 482-0657
Email: marcus@rkwholdings-example.com
Website: www.rkwholdings-example.com
Address: 418, 9th Street, Brooklyn NY 11218

Colors

Designer to choose colors to be used in the design.

Requirements
Nice to have
• Colors to match logo

```html
<!DOCTYPE html>
<html lang="en">
<head>
<meta charset="utf-8">
<title>RKW Holdings – Business Cards</title>
<link rel="stylesheet" href="https://fonts.googleapis.com/css2?family=Jost:wght@400&family=PT+Serif:wght@400&display=swap">
<style>
  :root {
    --page-bg: #f1f1f1;
    --card-bg: #ffffff;
    --brand-blue: #0e72a8;
    --ink-dark: #4a4a4a;
    --ink-mid: #555555;
    --card-edge: #d8d8d8;
  }
  * { margin: 0; padding: 0; box-sizing: border-box; }
  html, body {
    width: 1200px; height: 980px; overflow: hidden;
    background: var(--page-bg);
  }
  .canvas { position: relative; width: 1200px; height: 980px; }

  .card {
    position: absolute; left: 355px; width: 515px;
    background: var(--card-bg);
    border: 1px solid var(--card-edge);
  }
  .card--front { top: 166px; height: 315px; }
  .card--back  { top: 539px; height: 308px; }

  .brand {
    position: absolute; left: 0; right: 0;
    display: flex; align-items: center; justify-content: center; gap: 12px;
    font-family: "PT Serif", serif; color: var(--brand-blue);
  }
  .brand__square { background: var(--brand-blue); flex: none; }
  .card--front .brand { top: 78px; font-size: 22px; }
  .card--front .brand__square { width: 30px; height: 30px; }
  .card--back .brand { top: 190px; font-size: 38px; letter-spacing: 1px; }
  .card--back .brand__square { width: 44px; height: 44px; }

  .holder-name {
    position: absolute; top: 164px; left: 0; right: 0;
    text-align: center;
    font-family: "Jost", sans-serif; font-size: 26px; color: var(--ink-dark);
  }
  .holder-rule {
    position: absolute; top: 196px; left: 128px; width: 257px; height: 2px;
    background: var(--brand-blue); border-radius: 1px;
  }
  .contact {
    position: absolute; left: 0; right: 0;
    text-align: center;
    font-family: "PT Serif", serif; font-size: 12px; color: var(--ink-mid);
    letter-spacing: 0.6px;
  }
  .contact--line1 { top: 221px; }
  .contact--line1 span + span { margin-left: 20px; }
  .contact--line2 { top: 239px; }

  .web-band {
    position: absolute; left: 0; right: 0; bottom: 0; height: 30px;
    background: var(--brand-blue);
    display: flex; align-items: center; justify-content: center;
    font-family: "PT Serif", serif; font-size: 11px; font-weight: 400;
    letter-spacing: 3.5px; color: #2b2b2b;
  }
</style>
</head>
<body>
<main class="canvas">
  <section class="card card--front" aria-label="Business card front">
    <div class="brand">
      <span class="brand__square"></span>
      <span class="brand__name">RKW Holdings</span>
    </div>
    <h1 class="holder-name">Marcus Olvane</h1>
    <div class="holder-rule"></div>
    <p class="contact contact--line1"><span>Phone: (917) 482-0657</span><span>Email: marcus@rkwholdings-example.com</span></p>
    <p class="contact contact--line2">Adress : 418, 9th Street, Brooklyn NY 11218</p>
    <div class="web-band">www.rkwholdings-example.com</div>
  </section>

  <section class="card card--back" aria-label="Business card back">
    <div class="brand">
      <span class="brand__square"></span>
      <span class="brand__name">RKW Holdings</span>
    </div>
  </section>
</main>
</body>
</html>
```